Kestrel Builders Business Card Design Project

Clean sharp business card
Ability to write on back of card
Details for the card -
Address: PO Box 5867, Marrowvale, Qld, 4215
ABN: 47 305 961 220
BSA LIC 2650874
Ph: 07 3562 4470
Fax: 07 3562 4475
Email: kestrelbuilders@mailbrook.com.au

```html
<!DOCTYPE html>
<html lang="en">
<head>
<meta charset="utf-8">
<title>Kestrel Builders – Business Card</title>
<link href="https://fonts.googleapis.com/css2?family=Arimo:wght@400;700&display=swap" rel="stylesheet">
<style>
  :root {
    --backdrop: #3a1c1f;
    --card-edge: #ffffff;
    --card-face: #111111;
    --card-face-light: #1c1c1c;
    --text-light: #f2f2f2;
    --accent: #f28c1a;
  }
  html, body {
    margin: 0;
    padding: 0;
    width: 1200px;
    height: 1104px;
    overflow: hidden;
    background: var(--backdrop);
    font-family: "Arimo", Arial, sans-serif;
  }
  .canvas {
    position: relative;
    width: 1200px;
    height: 1104px;
  }
  .business-card {
    position: absolute;
    left: 150px;
    top: 282px;
    width: 900px;
    height: 540px;
    box-sizing: border-box;
    padding: 16px;
    background: var(--card-edge);
    border-radius: 44px;
  }
  .card-face {
    position: relative;
    width: 100%;
    height: 100%;
    border-radius: 30px;
    background: radial-gradient(ellipse at 40% 35%, var(--card-face-light), var(--card-face) 75%);
    overflow: hidden;
  }
  .brand {
    position: absolute;
    left: 100px;
    top: 150px;
    display: flex;
    align-items: center;
    gap: 16px;
  }
  .brand-dot {
    width: 22px;
    height: 22px;
    border-radius: 50%;
    background: var(--accent);
  }
  .brand-name {
    margin: 0;
    font-size: 50px;
    font-weight: 700;
    color: var(--text-light);
    letter-spacing: 0.5px;
    white-space: nowrap;
  }
  .contact {
    position: absolute;
    right: 60px;
    bottom: 70px;
    color: var(--text-light);
    font-size: 19px;
    line-height: 1.35;
    white-space: nowrap;
  }
  .contact p {
    margin: 0;
  }
  .contact .group + .group {
    margin-top: 16px;
  }
</style>
</head>
<body>
<main class="canvas">
  <section class="business-card" aria-label="Kestrel Builders business card">
    <div class="card-face">
      <div class="brand">
        <span class="brand-dot"></span>
        <h1 class="brand-name">Kestrel Builders</h1>
      </div>
      <div class="contact">
        <div class="group">
          <p>PO Box 5867, Marrowvale, Qld, 4215</p>
          <p>ABN: 47 305 961 220, BAS LIC 2650874</p>
        </div>
        <div class="group">
          <p>Ph: 07 3562 4470, Fax: 07 3562 4475</p>
          <p>Email: kestrelbuilders@mailbrook.com.au</p>
        </div>
      </div>
    </div>
  </section>
</main>
</body>
</html>
```